Advertising flyer for proofreading business.

Hello everyone,

I need an advertising flyer for a new proofreading company in Australia.

I would like your design in be in two sizes:
- A4 (to be posted on noticeboards),
- A6 (to be printed in larger quantity to give away)
(please see the size specification file attached).

The text file is attached (Ad Text) and it contains lots of information. Please feel free to include your choice of text from the text file, but please include Poster title, and highlight 'ESL' and students discounts.

I understand that it is impossible to include the same amount of information on A6 and A4, so please feel free to chose what fits on each of them, but please keep the design similar.

I have attached our company logo, but feel free to adjust it to the poster design (feel free to change the color as well). The original logo file contains circle around it, please feel free to remove it and include only the typeset as it can be seen here: http://www.lexmarka.com.au/.

Flyers will be printed, so please see the specification file for details.

I will do my best to respond to feedback as soon as possible.

I appreciate your participation, time and help,
Best wishes,
Bartosz

Target Market(s)

Students, authors

Industry/Entity Type

Business

Colors

Designer to choose colors to be used in the design.

Requirements
Must have
• It would be good if poster is easy to spot on busy noticeboards and attract attention.
• Please keep the poster in the positive/optimistic mood, and so that it focuses on students, maybe photos of graduates(?).
• Poster title,
• Please include the list of proof-read documents as they are described in the attached text file (Ad Text).
• Please highlight students discounts and ESL.
Nice to have
• I would like to leave the creative freedom to all designers so at this point I have not adjusted the Look and Feel sliders. Please feel free to offer your own take on this.
• It would be nice if most of the text could be fit to the poster.

```html
<!DOCTYPE html>
<html lang="en">
<head>
<meta charset="utf-8">
<title>Lexmarka – Professional English Language Proofreading</title>
<link href="https://fonts.googleapis.com/css2?family=Merriweather:wght@700;900&family=Roboto+Condensed:wght@700&family=Varela+Round&family=Open+Sans:wght@400;600;700&display=swap" rel="stylesheet">
<style>
  :root{
    --teal:#1fb79b;
    --teal-dark:#18a58b;
    --lime:#a6cf2f;
    --lime-light:#cfe36a;
    --yellow:#fdc70f;
    --ink:#333335;
    --charcoal:#3a3a3c;
    --white:#ffffff;
    --text:#3b3b3b;
  }
  *{margin:0;padding:0;box-sizing:border-box}
  html,body{width:873px;height:1200px;overflow:hidden;background:var(--white)}
  .flyer{position:relative;width:873px;height:1200px;overflow:hidden;font-family:"Open Sans",sans-serif;color:var(--text);background:var(--white)}

  .hero-photo{position:absolute;left:0;top:0;width:873px;height:600px;
    background:linear-gradient(160deg,#45b5a8 0%,#5fc0b3 40%,#8fd1c8 75%,#c8e8e3 100%);}
  .brand{position:absolute;left:38px;top:68px;display:flex;align-items:center;gap:12px;
    font-family:"Varela Round",sans-serif;font-size:60px;line-height:1;color:var(--white);letter-spacing:-1px}
  .brand-dot{width:22px;height:22px;border-radius:50%;background:var(--white)}

  .swoosh{position:absolute;left:0;top:440px}

  .tag{position:absolute;background:var(--charcoal);color:var(--white);font-family:"Merriweather",serif;font-weight:700;
    font-size:25px;padding:6px 14px 8px;border-radius:6px;transform:rotate(-19deg);white-space:nowrap;line-height:1.1}

  .headline{position:absolute;left:49px;top:618px;font-family:"Roboto Condensed",sans-serif;font-weight:700;line-height:1}
  .headline .lead{display:block;color:var(--teal);font-size:47px}
  .headline .main{display:block;color:var(--ink);font-size:47px;margin-top:2px;letter-spacing:.3px}

  .band{position:absolute;left:0;top:726px;width:873px;height:80px;display:flex}
  .band-esl{width:457px;background:var(--yellow);color:#222;font-family:"Varela Round",sans-serif;font-size:30px;line-height:1.12;padding:6px 0 0 44px}
  .band-scope{flex:1;background:var(--teal);color:var(--white);font-size:14.5px;line-height:1.6;padding:4px 34px 0 20px}

  .docs-title{position:absolute;left:49px;top:816px;font-family:"Varela Round",sans-serif;font-weight:400;color:var(--teal);font-size:27px}
  .docs{position:absolute;left:49px;top:864px;list-style:none;font-size:15px;line-height:24.6px;color:#444}
  .docs-2{left:257px}
  .docs li{display:flex;align-items:center;gap:6px}
  .tick{width:14px;height:12px;flex:none}

  .divider{position:absolute;left:460px;top:830px;width:1px;height:210px;background:#bdbdbd}
  .price-title{position:absolute;left:479px;top:815px;font-family:"Roboto Condensed",sans-serif;font-weight:700;font-size:21px;color:var(--ink)}
  .prices{position:absolute;left:479px;top:857px;width:352px;list-style:none;font-size:13.5px;line-height:17px;color:#444}
  .prices li{position:relative;padding-left:22px;margin-bottom:7px}
  .prices li::before{content:"";position:absolute;left:0;top:2px;width:13px;height:13px;border-radius:50%;
    background:radial-gradient(circle at 35% 35%,#c8e86a,#5f9a1a)}

  .contact{position:absolute;left:49px;top:1053px;font-family:"Varela Round",sans-serif;color:var(--ink)}
  .contact .ask{font-size:23px;line-height:1.15}
  .contact .line{font-family:"Open Sans",sans-serif;font-weight:700;font-size:25px;line-height:1.25;margin-top:3px}
  .contact .line + .line{margin-top:0}

  .footer-curve{position:absolute;left:0;top:1000px}
  .testimonial{position:absolute;left:480px;top:1086px;width:380px;text-align:right;color:var(--white)}
  .testimonial h3{font-family:"Merriweather",serif;font-weight:700;font-size:19px;color:var(--ink);text-align:center;margin-bottom:8px;padding-left:60px}
  .testimonial p{font-size:11.5px;line-height:14.5px}
  .testimonial .by{margin-top:4px;font-size:13px;font-weight:600}
  .testimonial .by strong{font-size:14.5px}
</style>
</head>
<body>
<div class="flyer">
  <div class="hero-photo" role="img" aria-label="Photo of two smiling students leaning on a desk with pens and notes, teal wall behind"></div>

  <div class="brand"><span class="brand-dot"></span>Lexmarka</div>

  <svg class="swoosh" width="873" height="200" viewBox="0 0 873 200" aria-hidden="true">
    <path d="M0 120 C120 60 260 150 430 160 C600 170 780 120 873 40 L873 90 C760 170 560 200 380 190 C220 180 110 150 0 175 Z" fill="var(--lime)"/>
    <path d="M0 175 C110 150 220 180 380 190 C560 200 760 170 873 90 L873 200 L0 200 Z" fill="var(--white)"/>
    <path d="M0 120 C120 60 260 150 430 160 C600 170 780 120 873 40 L873 20 C780 100 600 150 430 145 C260 140 120 40 0 100 Z" fill="var(--lime-light)" opacity=".7"/>
  </svg>

  <div class="tag" style="left:50px;top:464px">Proofreading by</div>
  <div class="tag" style="left:182px;top:480px">a native English</div>
  <div class="tag" style="left:290px;top:512px">speaker with</div>
  <div class="tag" style="left:404px;top:540px">an English</div>
  <div class="tag" style="left:490px;top:552px">Honours degree</div>

  <h1 class="headline"><span class="lead">PROFESSIONAL</span><span class="main">ENGLISH LANGUAGE PROOFREADING</span></h1>

  <div class="band">
    <div class="band-esl">Help with English as a<br>Second Language (ESL)</div>
    <div class="band-scope">Includes correct all English language errors, spelling and grammar mistakes, reference checking and editing for style, coherence and clarity.</div>
  </div>

  <h2 class="docs-title">We will proofread your:</h2>
  <ul class="docs">
    <li><svg class="tick" viewBox="0 0 14 12"><path d="M1 6 L5 10 L13 1" stroke="var(--teal)" stroke-width="2.6" fill="none"/></svg>Essays &amp; assignments</li>
    <li><svg class="tick" viewBox="0 0 14 12"><path d="M1 6 L5 10 L13 1" stroke="var(--teal)" stroke-width="2.6" fill="none"/></svg>Resumes</li>
    <li><svg class="tick" viewBox="0 0 14 12"><path d="M1 6 L5 10 L13 1" stroke="var(--teal)" stroke-width="2.6" fill="none"/></svg>Newsletters</li>
    <li><svg class="tick" viewBox="0 0 14 12"><path d="M1 6 L5 10 L13 1" stroke="var(--teal)" stroke-width="2.6" fill="none"/></svg>Websites</li>
    <li><svg class="tick" viewBox="0 0 14 12"><path d="M1 6 L5 10 L13 1" stroke="var(--teal)" stroke-width="2.6" fill="none"/></svg>Business correspondence</li>
    <li><svg class="tick" viewBox="0 0 14 12"><path d="M1 6 L5 10 L13 1" stroke="var(--teal)" stroke-width="2.6" fill="none"/></svg>Presentations &amp; speeches</li>
    <li><svg class="tick" viewBox="0 0 14 12"><path d="M1 6 L5 10 L13 1" stroke="var(--teal)" stroke-width="2.6" fill="none"/></svg>Brochures, catalogues &amp; media releases</li>
  </ul>
  <ul class="docs docs-2">
    <li><svg class="tick" viewBox="0 0 14 12"><path d="M1 6 L5 10 L13 1" stroke="var(--teal)" stroke-width="2.6" fill="none"/></svg>Theses</li>
    <li><svg class="tick" viewBox="0 0 14 12"><path d="M1 6 L5 10 L13 1" stroke="var(--teal)" stroke-width="2.6" fill="none"/></svg>Training manuals</li>
    <li><svg class="tick" viewBox="0 0 14 12"><path d="M1 6 L5 10 L13 1" stroke="var(--teal)" stroke-width="2.6" fill="none"/></svg>Advertising copy</li>
    <li><svg class="tick" viewBox="0 0 14 12"><path d="M1 6 L5 10 L13 1" stroke="var(--teal)" stroke-width="2.6" fill="none"/></svg>Novels &amp; short stories</li>
  </ul>

  <div class="divider"></div>
  <h2 class="price-title">Price guide:</h2>
  <ul class="prices">
    <li>Prices start at only $20 (short menus, flyers, letters).</li>
    <li>Discounts for not-for-profit organisations and students.</li>
    <li>Great student discount rate: $25 per hour (roughly 1000 words - 4 pages - of well-written text).</li>
    <li>Package deals on documents over 50,000 words.</li>
    <li>Fast, negotiable time-frames (same day service available by special arrangement).</li>
  </ul>

  <svg class="footer-curve" width="873" height="200" viewBox="0 0 873 200" aria-hidden="true">
    <path d="M345 200 C430 110 560 50 700 50 C780 50 840 70 873 82 L873 200 Z" fill="var(--lime)"/>
    <path d="M370 200 C450 120 575 62 710 62 C785 62 842 80 873 92 L873 200 Z" fill="var(--teal)"/>
    <path d="M470 120 C540 80 620 55 700 52 C780 50 840 68 873 80 L873 70 C830 52 770 38 700 40 C620 43 540 70 470 120 Z" fill="var(--ink)"/>
  </svg>

  <div class="contact">
    <div class="ask">Contact us for an<br>obligation FREE Quote:</div>
    <div class="line">0400 218 634 /</div>
    <div class="line">proofing@lexmarka.com.au</div>
  </div>

  <div class="testimonial">
    <h3>Testimonial...</h3>
    <p>Hannah understood our requirements quickly and has been fantastic at delivering quality work, on time and within agreed budget.&nbsp; It's a pleasure to work with her.</p>
    <div class="by"><strong>Carol Dunne,</strong> Operations Manager, Meridia AU</div>
  </div>
</div>
</body>
</html>
```